Christmas Card and envelope

A-7 Envelope with a 4-panel, drop-down, roll-fold Christmas card (finished size 7 x 18). Design direction and copy in the uploaded "White_Card.docx" file

```html
<!DOCTYPE html>
<html lang="en">
<head>
<meta charset="utf-8">
<title>The Story of the First Christmas Gift – Envelope and Roll-Fold Card</title>
<link rel="stylesheet" href="https://fonts.googleapis.com/css2?family=Great+Vibes&family=Raleway:wght@400;600;700&display=swap">
<style>
  :root{
    --board:#0f3159;
    --trim:#e2202a;
    --mark:#b25aa8;
    --guide:#d85aa0;
    --ink:#1d4f8f;
    --gold:#e7a534;
    --photo-frame:#d6ab4e;
  }
  *{box-sizing:border-box;margin:0;padding:0}
  html,body{width:1200px;height:1200px;overflow:hidden;background:var(--board)}
  body{position:relative;font-family:"Raleway",sans-serif;color:var(--ink)}
  .crop-marks{position:absolute;left:0;top:0}
  .piece{position:absolute;border:3px solid var(--trim);overflow:hidden}
  .safe{position:absolute;inset:5px;border:1px dashed var(--guide);pointer-events:none;z-index:5}
  .envelope{left:76px;top:234px;width:287px;height:278px}
  .card{top:234px;width:278px;height:709px}
  .card--outside{left:440px}
  .card--inside{left:787px}
  .panel{position:absolute;left:0;width:100%;height:177px}
  .panel--1{top:0;height:183px}
  .panel--2{top:183px}
  .panel--3{top:360px}
  .panel--4{top:537px;height:172px}
  .art{position:absolute}
  .abs{position:absolute}
  .title{position:absolute;color:#fff;line-height:1}
  .title .lead{font-family:"Raleway",sans-serif;font-size:11px;display:block;margin-bottom:2px}
  .title .of{font-family:"Raleway",sans-serif;font-size:8px;margin-right:4px}
  .title .script{font-family:"Great Vibes",cursive;font-size:25px;display:block;line-height:.88}
  .title--dark{color:var(--ink)}
  .address{font-size:5.6px;line-height:1.4;color:var(--ink)}
  .copy{position:absolute;left:0;width:100%;text-align:center;font-size:8.4px;line-height:1.3;color:var(--ink)}
  .copy p+p{margin-top:9px}
  .accent{color:var(--gold);font-weight:700;font-size:9px}
  .photo{position:absolute;width:64px;height:86px;border:3px solid var(--photo-frame)}
  .caption{position:absolute;width:80px;text-align:center;font-size:5.6px;line-height:1.3}
  .letter{position:absolute;left:30px;width:220px;font-size:7.4px;line-height:1.2;color:var(--ink)}
  .letter p{margin-bottom:8px}
  .letter .greet{font-weight:700;font-size:7.8px;margin-bottom:10px}
</style>
</head>
<body>

<svg class="crop-marks" width="1200" height="1200" aria-hidden="true">
  <g stroke="#b25aa8" stroke-width="1">
    <line x1="53" y1="229" x2="385" y2="229"/><line x1="53" y1="516" x2="385" y2="516"/>
    <line x1="71" y1="211" x2="71" y2="534"/><line x1="367" y1="211" x2="367" y2="534"/>
    <line x1="418" y1="229" x2="741" y2="229"/><line x1="418" y1="947" x2="741" y2="947"/>
    <line x1="436" y1="211" x2="436" y2="967"/><line x1="722" y1="211" x2="722" y2="967"/>
    <line x1="418" y1="564" x2="436" y2="564"/><line x1="722" y1="564" x2="741" y2="564"/>
    <line x1="765" y1="229" x2="1088" y2="229"/><line x1="765" y1="947" x2="1088" y2="947"/>
    <line x1="784" y1="211" x2="784" y2="967"/><line x1="1069" y1="211" x2="1069" y2="967"/>
    <line x1="765" y1="564" x2="784" y2="564"/><line x1="1069" y1="564" x2="1088" y2="564"/>
  </g>
</svg>

<section class="piece envelope">
  <div class="art" style="inset:0;background:linear-gradient(180deg,#3f8fd6 0%,#a9d0ee 22%,#eef4fa 26%,#ffffff 45%,#eef4fb 62%,#5ea7e0 82%,#1f5aa6 92%,#18386d 100%)" role="img" aria-label="Starry sky fading to white with three wise men on camels crossing dark blue dunes"></div>
  <div class="abs address" style="left:18px;top:88px">Martin &amp; Wendy Hale<br>4810 NE Alder Lane<br>Lakeview, OR 97641</div>
  <div class="title title--dark" style="left:130px;top:115px">
    <span class="lead" style="margin-left:28px">The story</span>
    <span class="script" style="margin-left:8px"><span class="of">of</span>the First</span>
    <span class="script">Christmass Gift</span>
  </div>
  <div class="safe"></div>
</section>

<section class="piece card card--outside">
  <div class="panel panel--1">
    <div class="art" style="inset:0;background:linear-gradient(180deg,#1d5ea9 0%,#3f8fd4 45%,#8cc2ea 72%,#2d6eb8 86%,#18386d 100%)" role="img" aria-label="Night sky with a bright star and three wise men on camels on a dune"></div>
    <div class="title" style="left:30px;top:41px">
      <span class="lead" style="margin-left:26px">The story</span>
      <span class="script" style="margin-left:10px"><span class="of">of</span>the First</span>
      <span class="script">Christmass Gift</span>
    </div>
  </div>
  <div class="panel panel--2">
    <div class="art" style="inset:0;background:radial-gradient(ellipse at 50% 55%,#ffffff 0%,#eaf4fb 45%,#bcdcf2 100%)" role="img" aria-label="Soft watercolour clouds with a faint star"></div>
    <div class="abs" style="left:0;width:100%;top:72px;text-align:center;font-family:'Great Vibes',cursive;font-size:33px;color:var(--ink)">Merry Christmas</div>
    <div class="abs address" style="left:0;width:100%;top:116px;text-align:center">Martin &amp; Wendy Hale<br>4810 NE Alder Lane<br>Lakeview, OR 97641</div>
  </div>
  <div class="panel panel--3">
    <div class="art" style="inset:0;background:linear-gradient(180deg,#fdf1cf 0%,#ffffff 40%,#fbe3a6 78%,#d9a245 100%)" role="img" aria-label="Warm golden watercolour with a gold silhouette of the nativity scene on a hill"></div>
    <div class="copy" style="top:23px">
      <p>For centuries, the tradition of giving gifts at Christmas<br>has been traced back to three wise men.<br>Guided by a miraculous star, they traveled far to bring<br>gifts of gold, frankincense, and myrrh<br>to a humble manger in Bethlehem.</p>
      <p>As magical as this story is, it wasn’t actually<br>the ffirst Christmas gift…</p>
    </div>
  </div>
  <div class="panel panel--4">
    <div class="art" style="inset:0;background:linear-gradient(180deg,#8fc4ea 0%,#e8f3fb 45%,#ffffff 70%,#a9d2f0 100%)" role="img" aria-label="Blue sky with soft clouds"></div>
    <div class="copy" style="top:12px">As we reflect on this incredible gift, we’re reminded of all<br>the blessings God has given us through the years.</div>
    <div class="photo" style="left:20px;top:37px;background:#8a8f78" role="img" aria-label="Family photo of Jordan, Kelsey, Ethan and Oliver"></div>
    <div class="photo" style="left:107px;top:37px;background:#9a9a94" role="img" aria-label="Family photo of Nate, Rowan and Felix"></div>
    <div class="photo" style="left:188px;top:37px;background:#a78a78" role="img" aria-label="Family photo of Carl, Megan, Stella, Walter and Blake"></div>
    <div class="caption" style="left:12px;top:127px">Jordan, Kelsey,<br>Ethan, &amp; Oliver</div>
    <div class="caption" style="left:99px;top:127px">Nate, Rowan, &amp; Felix</div>
    <div class="caption" style="left:180px;top:127px">Carl, Megan, Stella,<br>Walter, &amp; Blake</div>
    <div class="copy" style="top:145px;font-size:8.6px;line-height:1.1">And God has given us yet another gift we treasure …</div>
  </div>
  <div class="safe"></div>
</section>

<section class="piece card card--inside">
  <div class="panel panel--1">
    <div class="art" style="inset:0;background:radial-gradient(circle at 66% 46%,#fff3b8 0%,#7fbbe8 14%,#2f79c6 45%,#1f5fae 75%,#8cc4ea 100%)" role="img" aria-label="Starry night sky with a large golden star"></div>
  </div>
  <div class="panel panel--2">
    <div class="art" style="inset:0;background:linear-gradient(180deg,#e9f4fb 0%,#ffffff 35%,#d6eaf7 60%,#7fb6e0 82%,#1e4a86 100%)" role="img" aria-label="Soft clouds above a silhouette of the infant in a glowing manger on a hill"></div>
    <div class="copy" style="top:41px;font-size:8.6px">The real first Christmas gift was far more precious than<br>gold and spices. It was the gift of God’s own Son,<br><span class="accent">Jesus</span> — the greatest gift the world has ever known.</div>
  </div>
  <div class="panel panel--3">
    <div class="art" style="inset:0;background:radial-gradient(ellipse at 50% 50%,#fffbe8 0%,#fcefc3 60%,#e9c671 100%)" role="img" aria-label="Cream panel with an ornate gold scroll border"></div>
    <div class="abs" style="left:56px;top:29px;width:163px;height:113px;background:#fff;border:4px solid #d8b04f;outline:1px solid #c89a3a;outline-offset:-7px"></div>
    <div class="abs" style="left:0;width:100%;top:147px;text-align:center;font-size:5.8px;line-height:1.3;color:var(--ink)">Ben &amp; Laurel, you are one of God’s great gifts in our lives.<br>Thanks for the years of warmth and friendship.</div>
  </div>
  <div class="panel panel--4">
    <div class="art" style="inset:0;background:linear-gradient(180deg,#a3cff0 0%,#eef6fc 40%,#ffffff 65%,#b4d8f2 100%)" role="img" aria-label="Blue sky with soft clouds"></div>
    <div class="letter" style="top:17px">
      <p class="greet">Ben and Laurel,</p>
      <p>As our family exchanges gifts, shares laughter, and—in all likelihood—indulges in a bit too much food, we’ll take a moment to remember the gifts that cannot be wrapped or placed under the tree: the gift of friendship.</p>
      <p>Thank you for the gift of yours. May God fill your coming year with joy, abundance, and the warmth of family and friends.</p>
      <p>With much affection,</p>
    </div>
    <div class="abs" style="left:30px;top:140px;font-size:6.6px">Marty and Wendy</div>
    <div class="abs" style="left:106px;top:98px;width:82px;height:82px;border-radius:50%;border:3px solid #fff;background:#8f9a8e" role="img" aria-label="Portrait photo of Marty and Wendy"></div>
  </div>
  <div class="safe"></div>
</section>

</body>
</html>
```